Postcard Design

I am promoting a local school tax levy increase. I need a post card that helps market this. I saw a nice one online that someone did and I'd like something similar. I am attaching a picture of it.
Our election is April 7, 2015 and we want people to vote YES on it!
My bullet points will be: Our Children Our District Our Future
Our colors are Kelly Green and Canary but it is not mandatory that the postcards be those colors. I really like the image I sent you.
We also need to have the name of the ballot measure in smaller print under the date on the side which is: "Proposition Cedar Hollow East High School"
We also need it to say: "Advertisement paid for by the Cedar Hollow East High School Election Committee, Marla Keefe Treasurer.
For the back, you can put our name, address, and a picture of our proposed school which is image #2. You can also put: Call Doug Halvorsen @ 417-555-0187 for more information or to register for an upcoming Q&A forum.
Our name/Address is: Cedar Hollow East High School Election Committee
2756 County Road 3315
Larkdale, MO 65712
You can also include the chatterbook symbol on our card as we are on chatterbook and can include our web address as well which is: www.cedarholloweasthigh.com

Please spell check everything!

Please send me your ideas. I will need postage and address which I will provide once the proof is approved.
Thanks, Doug Halvorsen 417-555-0187

```html
<!DOCTYPE html>
<html lang="en">
<head>
<meta charset="utf-8">
<title>Cedar Hollow East High School – Vote Yes Postcard</title>
<link rel="stylesheet" href="https://fonts.googleapis.com/css2?family=Oswald:wght@500;700&family=Open+Sans:wght@400;700;800&display=swap">
<style>
  :root {
    --lime: #b5d334;
    --ink: #1f1d1c;
    --white: #ffffff;
    --backdrop: #e4d3b6;
    --sky-top: #4f86c6;
    --sky-low: #cfe0ee;
    --lawn: #7ea84a;
    --pavement: #c9ccc4;
    --band-blue: #3b7fc4;
  }
  html, body {
    margin: 0;
    padding: 0;
    width: 1200px;
    height: 500px;
    overflow: hidden;
    background: var(--backdrop);
  }
  p, h1, ul, address { margin: 0; padding: 0; }
  .canvas {
    position: relative;
    width: 1200px;
    height: 500px;
    background: var(--backdrop);
  }
  .card {
    position: absolute;
    top: 22px;
    height: 436px;
    background: var(--lime);
    color: var(--ink);
    overflow: hidden;
  }

  /* ---------- Front ---------- */
  .card--front { left: 25px; width: 555px; }
  .check-badge {
    position: absolute;
    left: 15px;
    top: 63px;
    width: 210px;
    height: 210px;
  }
  .headline {
    position: absolute;
    left: 233px;
    font-family: "Oswald", sans-serif;
    font-weight: 700;
    line-height: 1;
    color: var(--ink);
    transform-origin: left top;
    white-space: nowrap;
    letter-spacing: 0;
  }
  .headline--vote { top: -6px; font-size: 143px; transform: scaleX(0.8); }
  .headline--yes  { top: 109px; font-size: 181px; transform: scaleX(0.82); }
  .rule-vertical {
    position: absolute;
    left: 463px;
    top: 33px;
    width: 3px;
    height: 270px;
    background: var(--ink);
  }
  .date-line {
    position: absolute;
    left: 362px;
    top: 133px;
    width: 270px;
    height: 56px;
    transform: rotate(-90deg);
    text-align: center;
    font-family: "Oswald", sans-serif;
    font-weight: 700;
    font-size: 56px;
    line-height: 56px;
    letter-spacing: 6px;
    white-space: nowrap;
  }
  .measure-name {
    position: absolute;
    left: 380px;
    top: 153px;
    width: 290px;
    height: 16px;
    transform: rotate(-90deg);
    text-align: center;
    font-family: "Oswald", sans-serif;
    font-weight: 700;
    font-size: 13.5px;
    line-height: 16px;
    text-transform: uppercase;
    white-space: nowrap;
  }
  .rule-horizontal {
    position: absolute;
    left: 15px;
    width: 530px;
    height: 3px;
    background: var(--ink);
  }
  .rule-horizontal--top { top: 300px; }
  .rule-horizontal--bottom { top: 393px; height: 2px; }
  .pillars {
    position: absolute;
    left: 15px;
    top: 310px;
    width: 530px;
    list-style: none;
    display: flex;
    justify-content: space-between;
    font-family: "Open Sans", sans-serif;
    font-weight: 800;
    font-size: 21px;
    line-height: 32px;
    white-space: nowrap;
  }
  .pillars li + li::before { content: "|"; margin-right: 4px; font-weight: 400; }
  .social {
    position: absolute;
    right: 22px;
    top: 346px;
    display: flex;
    align-items: center;
    gap: 6px;
    font-family: "Open Sans", sans-serif;
    font-weight: 700;
    font-size: 12px;
    color: var(--ink);
  }
  .social__mark {
    width: 28px;
    height: 28px;
    background: var(--ink);
  }
  .web-address {
    position: absolute;
    left: 0;
    top: 368px;
    width: 555px;
    text-align: center;
    font-family: "Open Sans", sans-serif;
    font-weight: 700;
    font-size: 17px;
    line-height: 26px;
    letter-spacing: 1.5px;
  }
  .paid-for {
    position: absolute;
    left: 0;
    top: 405px;
    width: 555px;
    text-align: center;
    font-family: "Oswald", sans-serif;
    font-weight: 500;
    font-size: 10.5px;
    line-height: 16px;
    letter-spacing: 0.4px;
    text-transform: uppercase;
    white-space: nowrap;
  }

  /* ---------- Back ---------- */
  .card--back { left: 607px; width: 559px; }
  .school-rendering {
    position: absolute;
    left: 0;
    top: 0;
    width: 559px;
    height: 210px;
    background: linear-gradient(180deg, var(--sky-top) 0%, var(--sky-low) 52%, var(--lawn) 72%, var(--pavement) 88%, #e3e5e0 100%);
  }
  .rendering-title {
    position: absolute;
    left: 52px;
    top: 58px;
    color: var(--white);
    font-family: "Open Sans", sans-serif;
    line-height: 1.05;
  }
  .rendering-title__main { font-size: 22px; }
  .rendering-title__sub { font-size: 16px; }
  .rendering-caption {
    position: absolute;
    left: 0;
    top: 196px;
    width: 559px;
    text-align: center;
    font-family: "Open Sans", sans-serif;
    font-weight: 700;
    font-size: 13px;
    line-height: 16px;
    color: var(--ink);
  }
  .photo-band {
    position: absolute;
    left: 0;
    top: 210px;
    width: 559px;
    height: 6px;
    background: var(--band-blue);
  }
  .return-address {
    position: absolute;
    left: 55px;
    top: 242px;
    font-family: "Open Sans", sans-serif;
    font-style: normal;
    font-size: 15px;
    line-height: 21px;
  }
  .back-rule {
    position: absolute;
    left: 21px;
    top: 361px;
    width: 517px;
    height: 2px;
    background: var(--ink);
  }
  .call-to-action {
    position: absolute;
    left: 0;
    top: 370px;
    width: 559px;
    text-align: center;
    font-family: "Open Sans", sans-serif;
    font-weight: 700;
    font-size: 13px;
    line-height: 21px;
  }
  .call-to-action__contact { font-size: 15px; }
  .call-to-action__phone { font-size: 17px; }
</style>
</head>
<body>
<main class="canvas">

  <section class="card card--front" aria-label="Postcard front">
    <svg class="check-badge" viewBox="0 0 230 230" aria-hidden="true">
      <circle cx="115" cy="115" r="113" fill="var(--white)"/>
      <circle cx="115" cy="115" r="106" fill="var(--ink)"/>
      <polygon points="40,118 70,92 100,130 178,42 206,68 101,184" fill="var(--white)"/>
    </svg>

    <h1 class="headline headline--vote">VOTE</h1>
    <p class="headline headline--yes">YES</p>

    <div class="rule-vertical"></div>
    <p class="date-line">APRIL 7</p>
    <p class="measure-name">Proposition Cedar Hollow East High School</p>

    <div class="rule-horizontal rule-horizontal--top"></div>
    <ul class="pillars">
      <li>OUR CHILDREN</li>
      <li>OUR DISTRICT</li>
      <li>OUR FUTURE</li>
    </ul>

    <div class="social"><span>chatterbook</span><span class="social__mark"></span></div>
    <p class="web-address">www.cedarholloweasthigh.com</p>
    <div class="rule-horizontal rule-horizontal--bottom"></div>
    <p class="paid-for">Advertisement paid for by the Cedar Hollow East High School Election Committee, Marla Keefe, Treasurer</p>
  </section>

  <section class="card card--back" aria-label="Postcard back">
    <div class="school-rendering" role="img" aria-label="Architectural rendering of the proposed Cedar Hollow East High School building under a blue sky with lawn in front"></div>
    <div class="rendering-title">
      <div class="rendering-title__main">Cedar Hollow</div>
      <div class="rendering-title__sub">East High</div>
    </div>
    <p class="rendering-caption">Cedar Hollow East High Proposed School Building</p>
    <div class="photo-band"></div>

    <address class="return-address">
      Cedar Hollow East High School Election Committee<br>
      2756 County Road 3315<br>
      Larkdale, MO 65712
    </address>

    <div class="back-rule"></div>
    <p class="call-to-action">
      For more information or to register for an upcoming Q&amp;A forum, call:<br>
      <span class="call-to-action__contact">Doug Halvorsen @ <span class="call-to-action__phone">417.555.0187</span></span>
    </p>
  </section>

</main>
</body>
</html>
```